Graphic Insert - For Pillow Case

We are purchasing new pillow cases for a campaign we are running and need a graphic insert as part of our corporate branding and product description to go in our packaging. The packaging will be a clear plastic back with this graphic insert.

Size of Flyer: 6"x9"

Description: 440 Thread Count Egyptian Cotton Pillow Cases
Quantity: 2
Size of Pillow Case: Standard
Descriptive Words: Soft, Caress, Smooth, Gentle

Our website: www.valtrobe.com

Thanks,

Dale

```html
<!DOCTYPE html>
<html lang="en">
<head>
<meta charset="utf-8">
<title>Valtrobe Pillow Case Insert</title>
<link href="https://fonts.googleapis.com/css2?family=Roboto+Condensed:wght@300&family=Poppins:wght@400;700&family=Raleway:wght@400&display=swap" rel="stylesheet">
<style>
  :root {
    --bg: #e4e4e4;
    --paper: #ffffff;
    --slate: #5f6e75;
    --ink: #1c1c1c;
    --olive: #9a9a5c;
    --logo-grey: #6b6b6b;
    --photo-light: #eef3f7;
    --photo-mid: #d6e1ea;
    --photo-skin: #f1d8c4;
    --photo-warm: #f6e6d6;
  }
  * { margin: 0; padding: 0; box-sizing: border-box; }
  html, body { width: 1200px; height: 1000px; overflow: hidden; background: var(--bg); }
  .flyer {
    position: absolute; left: 300px; top: 50px;
    width: 600px; height: 900px;
    background: var(--paper);
    overflow: hidden;
  }
  .hero-photo {
    position: absolute; left: 0; top: 0; width: 600px; height: 660px;
    background:
      radial-gradient(ellipse 260px 160px at 380px 360px, var(--photo-skin) 0%, rgba(241,216,196,0) 100%),
      radial-gradient(ellipse 200px 220px at 500px 420px, var(--photo-warm) 0%, rgba(246,230,214,0) 100%),
      linear-gradient(180deg, var(--paper) 0%, var(--photo-light) 25%, var(--photo-mid) 55%, var(--photo-light) 85%, var(--paper) 100%);
  }
  .headline {
    position: absolute; left: 165px; top: 38px;
    font-family: "Roboto Condensed", sans-serif; font-weight: 300;
    color: var(--slate); line-height: 0.9; text-transform: uppercase;
  }
  .headline .lead { font-size: 78px; letter-spacing: 1px; }
  .headline .word { font-size: 50px; display: block; }
  .guide-line { position: absolute; left: 0; top: 0; }
  .product {
    position: absolute; left: 78px; top: 548px; width: 380px;
    font-family: "Poppins", sans-serif; color: var(--ink);
  }
  .product-title { font-weight: 700; font-size: 19px; line-height: 1.2; letter-spacing: 1.5px; text-transform: uppercase; word-spacing: 4px; }
  .product-spec { font-weight: 400; font-size: 11.5px; line-height: 1.35; margin-top: 6px; text-transform: uppercase; }
  .brand {
    position: absolute; right: 40px; top: 690px;
    display: flex; align-items: center; gap: 14px;
  }
  .brand-mark { width: 62px; height: 62px; border: 2px solid var(--logo-grey); border-radius: 50%; }
  .brand-name { font-family: "Raleway", sans-serif; font-weight: 400; font-size: 36px; letter-spacing: 5px; color: var(--logo-grey); }
  .website {
    position: absolute; left: 40px; top: 828px;
    font-family: "Raleway", sans-serif; font-size: 20px; letter-spacing: 9px; color: var(--olive);
  }
</style>
</head>
<body>
  <main class="flyer">
    <div class="hero-photo" role="img" aria-label="Photo of a woman sleeping peacefully on white cotton pillows in soft light"></div>

    <svg class="guide-line" width="600" height="900" aria-hidden="true">
      <polyline points="150,40 150,240 62,240 62,596" fill="none" stroke="var(--slate)" stroke-width="1.5"/>
      <circle cx="62" cy="600" r="7" fill="var(--slate)"/>
    </svg>

    <h1 class="headline">
      <span class="lead">Soft</span>
      <span class="word">Caress</span>
      <span class="word">Smooth</span>
      <span class="word">Gentle</span>
    </h1>

    <section class="product">
      <h2 class="product-title">440 Thread Count Egyptian Cotton Pillow Cases</h2>
      <p class="product-spec">Quantity: 2<br>Size of Pillow Case: Standard</p>
    </section>

    <div class="brand">
      <span class="brand-mark"></span>
      <span class="brand-name">VALTROBE</span>
    </div>

    <p class="website">www.valtrobe.com</p>
  </main>
</body>
</html>
```